Dane Calloway Photography

Would like the Business card to have a cool logo. I’m targeting wedding/ engagement: portrait photography. My phone number on it. And my business email address.

Target Market(s)

Wedding/portrait/engagement photography.

```html
<!DOCTYPE html>
<html lang="en">
<head>
<meta charset="utf-8">
<title>Dane Calloway Photography – Business Card</title>
<link href="https://fonts.googleapis.com/css2?family=Cinzel:wght@400&family=Arimo:wght@400&display=swap" rel="stylesheet">
<style>
  :root {
    --stage: #d9d9d9;
    --card-white: #ffffff;
    --brand-red: #a8141b;
    --brand-red-deep: #8e0f15;
    --ink: #2e2e2e;
    --rule: #9a9a9a;
    --ghost-light: #f3f3f3;
    --ghost-dark: #dedede;
  }
  * { margin: 0; padding: 0; box-sizing: border-box; }
  html, body {
    width: 1200px; height: 802px; overflow: hidden;
    background: var(--stage);
  }
  .canvas { position: relative; width: 1200px; height: 802px; }
  .card {
    position: absolute; top: 274px; width: 443px; height: 264px;
    box-shadow: 0 3px 8px rgba(0,0,0,0.28);
    overflow: hidden;
  }
  .card--front { left: 136px; background: var(--card-white); }
  .card--back { left: 624px; background: var(--brand-red); }

  .camera-motif {
    position: absolute; left: 0; top: 16px; width: 236px; height: 176px;
    background: radial-gradient(ellipse at 45% 50%, var(--ghost-dark) 0%, var(--ghost-light) 60%, rgba(255,255,255,0) 80%);
  }
  .wordmark {
    position: absolute; font-family: 'Cinzel', serif; font-weight: 400;
    line-height: 1;
  }
  .wordmark__name { display: block; white-space: nowrap; }
  .wordmark__tag { display: block; letter-spacing: 0.28em; margin-top: 5px; }
  .card--front .wordmark { left: 197px; top: 72px; color: var(--brand-red); }
  .card--front .wordmark__name { font-size: 27px; }
  .card--front .wordmark__tag { font-size: 11px; }

  .contact-name {
    position: absolute; left: 29px; top: 163px;
    font-family: 'Cinzel', serif; font-size: 15px; color: var(--ink);
    display: flex; align-items: center; width: 380px;
  }
  .contact-name__last { color: var(--brand-red); margin-left: 5px; }
  .contact-name__rule { flex: 1; height: 1px; background: var(--rule); margin-left: 8px; }

  .contact-list {
    position: absolute; left: 29px; top: 201px; list-style: none;
    font-family: 'Arimo', sans-serif; font-size: 12.5px; color: var(--ink);
  }
  .contact-list li { display: flex; align-items: center; height: 19px; }
  .contact-list svg { width: 15px; height: 15px; margin-right: 3px; }
  .website {
    position: absolute; right: 30px; top: 221px;
    font-family: 'Arimo', sans-serif; font-size: 12.5px; color: var(--ink);
  }
  .website__domain { color: var(--brand-red); }
  .base-band {
    position: absolute; left: 0; bottom: 0; width: 100%; height: 7px;
    background: var(--brand-red);
  }

  .icon-pattern {
    position: absolute; inset: 0;
    background: linear-gradient(135deg, var(--brand-red) 0%, var(--brand-red-deep) 50%, var(--brand-red) 100%);
  }
  .card--back .wordmark {
    left: 0; right: 0; top: 112px; text-align: center; color: #ffffff;
  }
  .card--back .wordmark__name { font-size: 34px; }
  .card--back .wordmark__tag { font-size: 14px; margin-top: 8px; }
</style>
</head>
<body>
<main class="canvas">
  <section class="card card--front">
    <div class="camera-motif" role="img" aria-label="Faint grey camera illustration"></div>
    <div class="wordmark">
      <span class="wordmark__name">DANE CALLOWAY</span>
      <span class="wordmark__tag">PHOTOGRAPHY</span>
    </div>
    <div class="contact-name">
      <span>MARCUS</span><span class="contact-name__last">ELLERY</span>
      <span class="contact-name__rule"></span>
    </div>
    <ul class="contact-list">
      <li>
        <svg viewBox="0 0 16 16" aria-hidden="true"><circle cx="8" cy="8" r="7" fill="none" stroke="#a8141b" stroke-width="1.4"/><path d="M5.5 4.5c-.6.6-.6 1.8.4 3.4s2.4 2.7 3.4 2.8c.7.1 1.3-.4 1.5-.9l-1.3-1-.8.6c-.8-.4-1.6-1.3-1.9-2.1l.6-.8-1-1.4z" fill="#a8141b"/></svg>
        555-214-8830
      </li>
      <li>
        <svg viewBox="0 0 16 16" aria-hidden="true"><circle cx="8" cy="8" r="7.5" fill="#a8141b"/><rect x="4.3" y="5.3" width="7.4" height="5.4" fill="none" stroke="#fff" stroke-width="1"/><path d="M4.3 5.3L8 8.3l3.7-3" fill="none" stroke="#fff" stroke-width="1"/></svg>
        dane@danecalloway.com
      </li>
    </ul>
    <div class="website">www.<span class="website__domain">danecalloway</span>.com</div>
    <div class="base-band"></div>
  </section>

  <section class="card card--back">
    <div class="icon-pattern" role="img" aria-label="Faint pattern of camera and film icons in deep red"></div>
    <div class="wordmark">
      <span class="wordmark__name">DANE CALLOWAY</span>
      <span class="wordmark__tag">PHOTOGRAPHY</span>
    </div>
  </section>
</main>
</body>
</html>
```